DESIGN OF STATIONERY - TALVORA MED

WE WORK IN THE FIELD OF HEALTH (IMAGING: MRI - CT ETC.).
WE WOULD LIKE TO CREATE THE ENTIRE STATIONERY DESIGN : LETTERHEAD, BUSINESS CARD, CALENDAR, INVOICES, CD HOLDER, ETC.

Target Market(s)

PERSONS UNDERTAKING HEALTH EXAMINATIONS

```html
<!DOCTYPE html>
<html lang="en">
<head>
<meta charset="utf-8">
<title>Talvora Med – Stationery</title>
<link href="https://fonts.googleapis.com/css2?family=Poppins:wght@400;600&display=swap" rel="stylesheet">
<style>
  :root {
    --teal: #00a79d;
    --band: #e6e7e8;
    --paper: #ffffff;
    --brand: #2a74c0;
    --ink: #231f20;
    --edge: #4d4d4d;
    --dash: #9a9a9a;
  }
  * { margin: 0; padding: 0; box-sizing: border-box; }
  html, body { width: 1072px; height: 1200px; overflow: hidden; }
  body { position: relative; background: var(--teal); font-family: "Poppins", Arial, sans-serif; color: var(--ink); }

  .backdrop { position: absolute; inset: 0; }

  .sheet {
    position: absolute;
    background: var(--paper);
    border: 0.6px solid var(--edge);
    overflow: hidden;
  }
  .sheet .band { position: absolute; left: 0; top: 0; width: 100%; background: var(--band); }
  .sheet .rule { position: absolute; bottom: 0; background: var(--teal); }

  .wordmark {
    position: absolute;
    font-family: "Poppins", Arial, sans-serif;
    font-weight: 600;
    color: var(--brand);
    white-space: nowrap;
    letter-spacing: 0.02em;
    line-height: 1;
    display: flex;
    align-items: center;
    gap: 0.3em;
  }
  .wordmark::after {
    content: "";
    width: 0.32em; height: 0.32em;
    border-radius: 50%;
    background: var(--brand);
  }

  .date { position: absolute; font-size: 5px; letter-spacing: 0.12em; }

  .contacts { position: absolute; display: grid; grid-auto-flow: column; }
  .contact { display: flex; align-items: center; gap: var(--gap); }
  .contact svg { width: var(--icon); height: var(--icon); flex: none; }
  .contact p { font-size: var(--fs); line-height: 1.25; font-weight: 400; }

  /* letterhead */
  .letterhead { left: 49px; top: 80px; width: 438px; height: 620px; }
  .letterhead .band { height: 123px; }
  .letterhead .rule { left: 26px; top: 87px; width: 4px; }
  .letterhead .wordmark { left: 25px; top: 42px; font-size: 17px; }
  .letterhead .date { left: 349px; top: 58px; }
  .letterhead .contacts { left: 72px; top: 566px; grid-template-columns: repeat(3, 114px); --icon: 14px; --fs: 4.4px; --gap: 6px; }

  /* business card */
  .card { left: 640px; top: 80px; width: 275px; height: 153px; }
  .card .band { height: 67px; }
  .card .rule { left: 18px; top: 49px; width: 2px; }
  .card .wordmark { left: 18px; top: 25px; font-size: 10px; }
  .card .contacts { left: 44px; top: 111px; grid-template-columns: repeat(3, 75px); --icon: 10px; --fs: 2.6px; --gap: 4px; }

  /* envelope */
  .envelope { left: 543px; top: 368px; width: 470px; height: 203px; }
  .envelope .band { height: 100px; }
  .envelope .rule { left: 40px; top: 64px; width: 2px; }
  .envelope .wordmark { left: 38px; top: 31px; font-size: 15px; }
  .envelope .contacts { left: 111px; top: 149px; grid-template-columns: repeat(3, 103px); --icon: 13px; --fs: 3.8px; --gap: 6px; }

  .die-lines { position: absolute; left: 0; top: 0; }
  .die-lines text { font-family: "Poppins", Arial, sans-serif; fill: var(--ink); }
  .die-lines .svg-wordmark { font-weight: 600; fill: var(--brand); letter-spacing: 0.02em; }
</style>
</head>
<body>

<svg width="0" height="0" style="position:absolute" aria-hidden="true">
  <defs>
    <symbol id="icon-pin" viewBox="0 0 24 24">
      <path d="M12 2.5a7 7 0 0 0-7 7c0 5 7 12 7 12s7-7 7-12a7 7 0 0 0-7-7z" fill="none" stroke="#2a74c0" stroke-width="2"/>
      <circle cx="12" cy="9.5" r="2.6" fill="#2a74c0"/>
    </symbol>
    <symbol id="icon-mail" viewBox="0 0 24 24">
      <circle cx="12" cy="12" r="10.5" fill="none" stroke="#2a74c0" stroke-width="1.6"/>
      <rect x="6" y="8" width="12" height="8.5" fill="none" stroke="#2a74c0" stroke-width="1.3"/>
      <path d="M6 8l6 5 6-5M6 16.5l4.4-4.3M18 16.5l-4.4-4.3" fill="none" stroke="#2a74c0" stroke-width="1.1"/>
    </symbol>
    <symbol id="icon-phone" viewBox="0 0 24 24">
      <circle cx="12" cy="12" r="10.5" fill="none" stroke="#2a74c0" stroke-width="1.6"/>
      <path d="M8.6 6.8l1.8-.3 1.2 2.8-1.3 1.1c.7 1.5 1.8 2.6 3.3 3.3l1.1-1.3 2.8 1.2-.3 1.8c-.2.6-.8 1-1.5 1-4.8-.4-8.3-3.9-8.7-8.7 0-.7.4-1.3 1.6-.9z" fill="none" stroke="#2a74c0" stroke-width="1.3" stroke-linejoin="round"/>
    </symbol>
  </defs>
</svg>

<svg class="backdrop" width="1072" height="1200" aria-hidden="true">
  <polygon points="1072,556 1072,1200 0,1200 0,1063" fill="#ffffff"/>
</svg>

<section class="sheet letterhead" aria-label="Letterhead">
  <div class="band"></div>
  <div class="rule"></div>
  <div class="wordmark">TALVORA MED</div>
  <div class="date">30 May 2023</div>
  <div class="contacts">
    <div class="contact"><svg><use href="#icon-pin"/></svg><p>Lorem ipsum dolor sit<br>amet, consectetuer<br>adipiscing elit, sed</p></div>
    <div class="contact"><svg><use href="#icon-mail"/></svg><p>Lorem ipsum dolor sit<br>amet, consectetuer<br>adipiscing elit, sed</p></div>
    <div class="contact"><svg><use href="#icon-phone"/></svg><p>Lorem ipsum dolor sit<br>amet, consectetuer<br>adipiscing elit, sed</p></div>
  </div>
</section>

<section class="sheet card" aria-label="Business card">
  <div class="band"></div>
  <div class="rule"></div>
  <div class="wordmark">TALVORA MED</div>
  <div class="contacts">
    <div class="contact"><svg><use href="#icon-pin"/></svg><p>Lorem ipsum dolor sit<br>amet, consectetuer<br>adipiscing elit, sed</p></div>
    <div class="contact"><svg><use href="#icon-mail"/></svg><p>Lorem ipsum dolor sit<br>amet, consectetuer<br>adipiscing elit, sed</p></div>
    <div class="contact"><svg><use href="#icon-phone"/></svg><p>Lorem ipsum dolor sit<br>amet, consectetuer<br>adipiscing elit, sed</p></div>
  </div>
</section>

<svg class="die-lines" width="1072" height="1200" aria-label="Envelope flap, folder die-cut and CD label">
  <defs>
    <clipPath id="folder-shape">
      <path d="M45 804H318L324 762H584L590 804H658Q670 804 670 816V1076Q670 1088 658 1088H590L587 1129H327L321 1088H45Z"/>
    </clipPath>
    <clipPath id="disc-shape">
      <circle cx="858" cy="939" r="159"/>
    </clipPath>
  </defs>

  <!-- envelope flap -->
  <polygon class="envelope-flap" points="543,368.5 566,332 993,332 1013,368.5" fill="#e6e7e8" stroke="#4d4d4d" stroke-width="0.6"/>

  <!-- folder die-cut -->
  <g class="folder">
    <g clip-path="url(#folder-shape)">
      <rect x="40" y="755" width="640" height="380" fill="#ffffff"/>
      <rect x="40" y="755" width="640" height="164" fill="#e6e7e8"/>
      <rect x="350" y="889" width="2.4" height="245" fill="#00a79d"/>
    </g>
    <path d="M45 804H318L324 762H584L590 804H658Q670 804 670 816V1076Q670 1088 658 1088H590L587 1129H327L321 1088H45Z" fill="none" stroke="#4d4d4d" stroke-width="0.6"/>
    <g fill="none" stroke="#9a9a9a" stroke-width="0.8" stroke-dasharray="3 2">
      <path d="M51 810H654Q664 810 664 820V1072Q664 1082 654 1082H51Z"/>
      <path d="M322 810V1082M588 810V1082"/>
      <path d="M323 810L329 768H579L585 810"/>
      <path d="M324 1082L330 1123H584L586 1082"/>
    </g>
    <text class="svg-wordmark" x="347" y="871" font-size="17">TALVORA MED</text>
    <circle cx="466" cy="865" r="2.7" fill="#2a74c0"/>
    <g font-size="2.6">
      <use href="#icon-pin" x="377" y="1030" width="10" height="10"/>
      <text x="391" y="1034"><tspan x="391">Lorem ipsum dolor sit</tspan><tspan x="391" dy="3.2">amet, consectetuer</tspan><tspan x="391" dy="3.2">adipiscing elit, sed</tspan></text>
      <use href="#icon-mail" x="448" y="1030" width="10" height="10"/>
      <text x="462" y="1034"><tspan x="462">Lorem ipsum dolor sit</tspan><tspan x="462" dy="3.2">amet, consectetuer</tspan><tspan x="462" dy="3.2">adipiscing elit, sed</tspan></text>
      <use href="#icon-phone" x="519" y="1030" width="10" height="10"/>
      <text x="533" y="1034"><tspan x="533">Lorem ipsum dolor sit</tspan><tspan x="533" dy="3.2">amet, consectetuer</tspan><tspan x="533" dy="3.2">adipiscing elit, sed</tspan></text>
    </g>
  </g>

  <!-- CD label -->
  <g class="disc">
    <g clip-path="url(#disc-shape)">
      <rect x="699" y="780" width="318" height="318" fill="#ffffff"/>
      <rect x="699" y="780" width="318" height="159" fill="#e6e7e8"/>
      <rect x="761" y="878" width="2.2" height="200" fill="#00a79d"/>
    </g>
    <circle cx="858" cy="939" r="159" fill="none" stroke="#4d4d4d" stroke-width="0.6"/>
    <circle cx="858" cy="939" r="40" fill="#ffffff" stroke="#c8c8c8" stroke-width="0.6"/>
    <circle cx="858" cy="939" r="17" fill="#231f20"/>
    <text class="svg-wordmark" x="760" y="865" font-size="14">TALVORA MED</text>
    <circle cx="858" cy="860" r="2.2" fill="#2a74c0"/>
    <g font-size="2.4">
      <use href="#icon-pin" x="773" y="1014" width="9" height="9"/>
      <text x="786" y="1017"><tspan x="786">Lorem ipsum dolor sit</tspan><tspan x="786" dy="3">amet, consectetuer</tspan><tspan x="786" dy="3">adipiscing elit, sed</tspan></text>
      <use href="#icon-mail" x="847" y="1014" width="9" height="9"/>
      <text x="860" y="1017"><tspan x="860">Lorem ipsum dolor sit</tspan><tspan x="860" dy="3">amet, consectetuer</tspan><tspan x="860" dy="3">adipiscing elit, sed</tspan></text>
      <use href="#icon-phone" x="922" y="1014" width="9" height="9"/>
      <text x="935" y="1017"><tspan x="935">Lorem ipsum dolor sit</tspan><tspan x="935" dy="3">amet, consectetuer</tspan><tspan x="935" dy="3">adipiscing elit, sed</tspan></text>
    </g>
  </g>
</svg>

<section class="sheet envelope" aria-label="Envelope">
  <div class="band"></div>
  <div class="rule"></div>
  <div class="wordmark">TALVORA MED</div>
  <div class="contacts">
    <div class="contact"><svg><use href="#icon-pin"/></svg><p>Lorem ipsum dolor sit<br>amet, consectetuer<br>adipiscing elit, sed</p></div>
    <div class="contact"><svg><use href="#icon-mail"/></svg><p>Lorem ipsum dolor sit<br>amet, consectetuer<br>adipiscing elit, sed</p></div>
    <div class="contact"><svg><use href="#icon-phone"/></svg><p>Lorem ipsum dolor sit<br>amet, consectetuer<br>adipiscing elit, sed</p></div>
  </div>
</section>

</body>
</html>
```